Letterhead design - Ferrowby Group

We have just had our Logo created and our now wantng a letterhead design to incorporate this. Please use the same colours as in the logo, which is attached.
Please use the company details below
P O Box 86, Westbrook 7315
Ph: 03 491 2753
dale@ferrowbygroup.co.nz
We would like a professional look
We need an overall letterhead design for our varied group of buisinesses which are based in NZ and overseas. We grow and develop buisinesses. Our companies began in NZ but we now have branches overseas as well. People are our greatest asset and we employ some incredible staff. Our buisinesses are scientific, innovative and growing in size and expertise with a financial base.

Target Market(s)

Professionals

Industry/Entity Type

Investment

Requirements
Must have
• Easy to read.
• Please use the same colours as in the logo
• Please use the company details below
• P O Box 86, Westbrook 7315
• Ph: 03 491 2753
• dale@ferrowbygroup.co.nz

```html
<!DOCTYPE html>
<html lang="en">
<head>
<meta charset="utf-8">
<title>Ferrowby Group Letterhead</title>
<link rel="stylesheet" href="https://fonts.googleapis.com/css2?family=Montserrat:wght@700&family=Questrial&display=swap">
<style>
  :root {
    --green: #1fa667;
    --grey: #58595b;
    --ink: #3c3c3c;
    --paper: #ffffff;
    --backdrop: #e4d8c2;
  }
  * { box-sizing: border-box; margin: 0; padding: 0; }
  html, body { width: 1200px; height: 899px; overflow: hidden; }
  body { background: var(--backdrop); font-family: "Questrial", sans-serif; color: var(--ink); }

  .letterhead {
    position: absolute; left: 303px; top: 30px;
    width: 594px; height: 840px;
    background: var(--paper);
    box-shadow: 0 6px 22px rgba(0,0,0,.18);
    overflow: hidden;
  }
  .side-band {
    position: absolute; left: 0; top: 22px;
    width: 58px; height: 818px;
    background: var(--green);
  }
  .side-band .side-mark {
    position: absolute; left: 14px; bottom: 26px;
    width: 30px; height: 30px; background: #fff;
  }

  .masthead {
    position: absolute; left: 140px; top: 62px; width: 360px;
    text-align: center;
  }
  .brand { display: flex; align-items: center; justify-content: center; gap: 10px; white-space: nowrap; }
  .brand-square { flex: none; width: 28px; height: 28px; background: var(--green); }
  .brand-name {
    font-family: "Montserrat", sans-serif; font-weight: 700;
    font-size: 24px; letter-spacing: 1px; color: var(--green);
    white-space: nowrap;
  }
  .masthead-rule { height: 2px; background: var(--green); margin: 12px 0 8px; }
  .website { font-size: 13px; letter-spacing: 2px; color: var(--grey); }

  .letter-body {
    position: absolute; left: 120px; top: 190px; width: 400px;
    font-size: 10.5px; line-height: 1.65; text-align: justify;
  }
  .letter-body p { margin-bottom: 16px; }

  .signature { position: absolute; left: 420px; top: 585px; }
  .signature .name { font-size: 12px; color: var(--ink); }
  .signature .role { font-size: 8px; color: var(--grey); margin-top: 2px; }

  .contact-bar {
    position: absolute; left: 58px; right: 0; top: 795px; height: 30px;
    background: var(--grey); display: flex;
  }
  .contact-item {
    flex: 1; position: relative;
    color: #fff; font-size: 10px; letter-spacing: .5px; white-space: nowrap;
    display: flex; align-items: center; justify-content: center;
    border-left: 2px solid var(--paper);
  }
  .contact-item:first-child { border-left: none; }
  .contact-icon {
    position: absolute; top: -9px; left: 50%; margin-left: -9px;
    width: 18px; height: 18px; border-radius: 50%; background: var(--green);
    display: flex; align-items: center; justify-content: center;
  }
</style>
</head>
<body>
  <main class="letterhead">
    <div class="side-band"><div class="side-mark"></div></div>

    <header class="masthead">
      <div class="brand">
        <span class="brand-square"></span>
        <span class="brand-name">FERROWBY GROUP</span>
      </div>
      <div class="masthead-rule"></div>
      <div class="website">ferrowbygroup.co.nz</div>
    </header>

    <section class="letter-body">
      <p>Lorem ipsum dolor sit amet, consectetur adipiscing elit. Donec orci purus, luctus vitae dignissim eu, iaculis sed purus. Vivamus faucibus ipsum nec aliquet viverra, leo mauris condimentum ligula, sit amet sagittis enim ligula quis arcu. Nam egestas tortor id nisi porttitor mattis. In tortor ante, ultricies in suscipit a, tempus non massa. Vivamus et auctor mi. Fusce vel massa nulla. Phasellus nec eros mauris, et scelerisque orci. Donec malesuada orci vitae nulla accumsan porta a id massa.</p>
      <p>Aenean magna eget tincidunt semper, odio nibh rutrum mi, id feugiat ante nisl eu risus. Vestibulum nunc ornare, rhoncus a placerat in, ultricies in mi. Cras mattis varius eros, vel fringilla nisi suscipit eget. Quisque scelerisque sagittis nulla at porttitor. Mauris a justo et tellus interdum tristique. Sed id augue vitae urna euismod commodo aliquet a quam. Pellentesque arcu velit, cursus et malesuada ut, consequat et diam.</p>
      <p>Integer faucibus ultricies. Morbi semper, est id tincidunt gravida, sem arcu adipiscing lacus, ac bibendum nulla leo eu purus. Quisque nec diam sed risus consectetur a accumsan quis nibh. Vestibulum id purus lorem. Donec eu magna a metus ornare faucibus. Fusce aliquet faucibus ultricies. Morbi semper, est id tincidunt gravida, sem arcu adipiscing lacus, ac bibendum nulla leo eu purus. Quisque nec diam sed risus consectetur a accumsan quis nibh. Vestibulum id purus lorem.</p>
    </section>

    <div class="signature">
      <div class="name">Owen Hartley</div>
      <div class="role">Co-Founder &amp; CEO</div>
    </div>

    <footer class="contact-bar">
      <div class="contact-item">
        <span class="contact-icon"><svg width="10" height="10" viewBox="0 0 24 24"><path fill="#fff" d="M6.6 10.8a15.1 15.1 0 0 0 6.6 6.6l2.2-2.2c.3-.3.7-.4 1-.2 1.1.4 2.3.6 3.6.6.6 0 1 .4 1 1V20c0 .6-.4 1-1 1A17 17 0 0 1 3 4c0-.6.4-1 1-1h3.5c.6 0 1 .4 1 1 0 1.3.2 2.5.6 3.6.1.3 0 .7-.2 1z"/></svg></span>
        03 491 2753
      </div>
      <div class="contact-item">
        <span class="contact-icon"><svg width="10" height="10" viewBox="0 0 24 24"><path fill="#fff" d="M3 5h18v14H3z"/><path fill="none" stroke="#1fa667" stroke-width="2" d="M3 5l9 7 9-7"/></svg></span>
        dale@ferrowbygroup.co.nz
      </div>
      <div class="contact-item">
        <span class="contact-icon"><svg width="10" height="10" viewBox="0 0 24 24"><path fill="#fff" d="M12 2a7 7 0 0 0-7 7c0 5 7 13 7 13s7-8 7-13a7 7 0 0 0-7-7zm0 9.5A2.5 2.5 0 1 1 12 6.5a2.5 2.5 0 0 1 0 5z"/></svg></span>
        P O Box 86, Westbrook 7315
      </div>
    </footer>
  </main>
</body>
</html>
```